Outdoor sign for Brindle Auto Restoration

I need a horizontal 4'x 8' outdoor roadside sign for my classic auto restoration business. I have uploaded colors and our logo. Needs the Brindle name, a prominent Classic AUTO RESTORATION, phone number and website. We rebuild and restore vintage cars, trucks and 4x4s. I'd like something clean but possibly retro. Classic Auto Restoration is more important than the Brindle name. It needs to be visible and readable from the street. NO CLIP ART

Target Market(s)

Customers who need their vintage care restored or upgraded. Men and women ages 25-75

Industry/Entity Type

Automotive

Colors
FFC000
F8CF3A
FAE287
FDF2CF
FEFAEE

Requirements
Must have
• Legible. Bright. Readable as a backlit 4' x 8' large horizontal sign (roughly 120cm X 240cm)
Nice to have
• Use of the Brindle logo/type, Complete or Classic before prominent AUTO RESTORATION
Should not have
• Clip art of old cars or icons. And we don't want the Brindle Logo from the website because it wont be legible from the road. I have included the Illustrator file for Brindle text in the uploads

```html
<!DOCTYPE html>
<html lang="en">
<head>
<meta charset="utf-8">
<title>Brindle Classic Auto Restoration – Roadside Sign</title>
<link href="https://fonts.googleapis.com/css2?family=Archivo:wdth,wght@125,800;125,900&family=Oswald:wght@700&family=Roboto+Condensed:wght@700&display=swap" rel="stylesheet">
<style>
  :root {
    --backdrop: #f9d68b;
    --sign-dark: #2b2321;
    --sign-gold: #f4ae00;
  }
  html, body {
    margin: 0;
    padding: 0;
    width: 1200px;
    height: 728px;
    overflow: hidden;
    background: var(--backdrop);
  }
  .sign {
    display: block;
    width: 1200px;
    height: 728px;
  }
  .sign__panel { fill: var(--sign-dark); }
  .sign__band { fill: var(--sign-gold); }
  .sign__brand {
    fill: var(--sign-gold);
    font-family: "Oswald", "Arial Narrow", sans-serif;
    font-weight: 700;
    font-size: 66px;
  }
  .sign__headline {
    fill: var(--sign-gold);
    font-family: "Archivo", "Arial Black", sans-serif;
    font-stretch: 125%;
    font-weight: 900;
    font-size: 108px;
  }
  .sign__phone {
    fill: var(--sign-gold);
    font-family: "Roboto Condensed", "Arial Narrow", sans-serif;
    font-weight: 700;
    font-size: 64px;
  }
  .sign__web {
    fill: var(--sign-dark);
    font-family: "Archivo", "Arial Black", sans-serif;
    font-stretch: 125%;
    font-weight: 800;
    font-size: 44px;
  }
</style>
</head>
<body>
<svg class="sign" viewBox="0 0 1200 728" xmlns="http://www.w3.org/2000/svg" role="img" aria-label="Brindle Classic Auto Restoration sign">
  <defs>
    <filter id="panel-shadow" x="-5%" y="-5%" width="110%" height="115%">
      <feDropShadow dx="2" dy="3" stdDeviation="2" flood-color="#000" flood-opacity="0.35"/>
    </filter>
  </defs>
  <g filter="url(#panel-shadow)">
    <rect class="sign__panel" x="72" y="100" width="1056" height="528"/>
    <rect class="sign__band" x="72" y="557" width="1056" height="71"/>
  </g>
  <text class="sign__brand" x="117" y="187" textLength="280" lengthAdjust="spacingAndGlyphs">BRINDLE</text>
  <text class="sign__headline" x="117" y="311" textLength="966" lengthAdjust="spacingAndGlyphs">CLASSIC AUTO</text>
  <text class="sign__headline" x="158" y="440" textLength="917" lengthAdjust="spacingAndGlyphs">RESTORATION</text>
  <text class="sign__phone" x="443" y="523" textLength="355" lengthAdjust="spacingAndGlyphs">501-555-0142</text>
  <text class="sign__web" x="600" y="609" text-anchor="middle" textLength="620" lengthAdjust="spacingAndGlyphs">brindle autoworks.com</text>
</svg>
</body>
</html>
```